Systems and Technology Consultants - Website

Design & Build a website for a new company which operates in the Systems and Technology space for Transportation, Government and Commercial sectors.

Overall design should be minimalist in nature.
Should also have a feed that provides news and event updates on the main page.
Logo has already been awarded and should be incorporated into the site.

We like the overall layout, functionality and simplicity of the below sites. Submitted designs could be similar to or a combination of the aspects on these sites, or perhaps a whole different concept - we are open to new ideas.
Vortrane.com
Merp.it

Update 1 Dated 27 May 2014

All I am moving away from the Merp.it website and would like it to be more aligned with Vortrane.com not only in layout but in functionality. I will be extending the deadline of this design brief for two weeks to incorporate additional requirements and will add addtional funding to the project.

Apologies for not having more information available to provide but with so many submissions its getting confusing.

Thanks Dermot
Updates

Please note that the brief has been updated and the deadline has been extended.

Important: We will need two language versions of the website, English and Arabic; the website is hosted on HostPeak

Hello All, Thank you for your submissions. We have narrowed it down to the final 6 designers and I just wanted to take a moment and provide a bit of feedback regarding the concepts that we like and the modifications we are looking for. First, let me mention some of the design functions we like. - At the top of the homepage we really like the "region" or "language" tab so that the website can be viewed in both English and Arabic. - We like the homepage to have clear color variation so that the different sections of the homepage are distinct. Additionally, we like the bottom portion of the homepage to be in red. We feel that draws attention to our contact information. Again, we would like the colors to integrate black, gray-scale, red, etc. - Having a search tab at the top of the home page, or integrated into the main image, so that the site is easy to navigate. - We especially like the main image to have the scrolling tabs at the bottom so it is easy to browse the services offered (Consultancy, Solutions Architecture, Masters Systems Integration, Independent Design Review). - In regards to the services offered tab we really like the idea that a few people presented that have the outside of our logo with an icon in the middle of consultancy, solutions, etc., etc. Secondly, as mentioned in our brief we really enjoy the design of vortrane site. Specially, we enjoy the strong iconic images they use, the way the tabs at the top scroll easily, and contact us page that generates an email. Lastly, I've included some photos of the concept we have been working on. What we are trying to demonstrate is how our company offers a range of services that are essentially linked together. We provide individual services that when combined present the full service package. We would like this concept to be integrated into the over concept of our website. Please feel free to ask for clarification of any of the above points or contact us if you have any additional questions. We appreciate all of your hard work and are very excited to see the updated designs. Best, Miriam Dowbrook Plenvaro Senior Program Manager miriam.dowbrook@plenvaro-mail.com

Industry/Entity Type

Government

Font styles to use
Serif
Sans Serif

Requirements
Must have
• Must work on/adapt to various/mobile devices (responsive)
Must be simple and straightforward
Colors should be in line/matching with logo
2 language versions: English and Arabic (no Thai)
Services should be the first group/row of items after/below the main image
Note: the website will be hosted by hostpeak
Nice to have
• Submit feedback form
What's New section
The banner at the bottom of the site should not be too large; we would like a narrow one more
It would be nice if the header/top banner (with Home, About, etc. tabs) could stay in place as you scroll down (like Vortrane and Chatterly)
We will likely only use one image with a Company slogan on the Home page rather than a carousel of images to rotate through
Should not have
• This is the existing website: http://www.plenvaro-example.org
We do not like the animation, the way the banner icons/titles bounce
Not simple enough, we don't like the functionality or how pages load so slowly
We do not like the logo centered - it should be at the left
The banner and its tabs should not be towards the right, we would like them to be centered, to go all the way across and to be below the logo

```html
<!DOCTYPE html>
<html lang="en">
<head>
<meta charset="utf-8">
<title>Plenvaro International</title>
<link href="https://fonts.googleapis.com/css2?family=Lato:wght@300;400;700;900&display=swap" rel="stylesheet">
<style>
:root{
  --red:#e8383f;
  --ink:#333b40;
  --muted:#9aa1a5;
  --mist:#eef3f5;
  --footer:#2e3338;
  --footer-deep:#262a2f;
  --footer-text:#8e969b;
  --white:#ffffff;
}
*{margin:0;padding:0;box-sizing:border-box}
html,body{width:1012px;height:1200px;overflow:hidden;background:var(--white)}
body{font-family:'Lato',sans-serif;color:var(--ink);position:relative}
.abs{position:absolute}

.topbar{left:0;top:0;width:1012px;height:25px;background:var(--red);color:var(--white);font-size:7.5px}
.topbar .item{position:absolute;top:8px;display:flex;align-items:center;gap:6px;white-space:nowrap}

.header{left:0;top:25px;width:1012px;height:57px;background:var(--white);border-bottom:1px solid #e6e6e6}
.brand{left:218px;top:20px;display:flex;align-items:center;gap:8px;color:var(--red);font-weight:700;font-size:15px;letter-spacing:3px}
.brand .mark{width:12px;height:12px;background:var(--red)}
.nav a{position:absolute;top:24px;font-size:8.5px;color:#555;text-decoration:none}

.hero{left:0;top:82px;width:1012px;height:316px;overflow:hidden}
.hero-photo{position:absolute;inset:0;background:linear-gradient(90deg,#c9d9e6 0%,#d8cbb4 30%,#b7a78d 50%,#6b6058 70%,#8a5a3c 85%,#a86f44 100%)}
.hero-panel{position:absolute;left:514px;top:0;width:301px;height:316px;background:rgba(70,70,72,.72)}
.hero-kicker{left:549px;top:154px;font-size:19px;font-weight:300;color:var(--red);letter-spacing:.3px;line-height:22px;white-space:nowrap}
.hero-title{left:548px;top:173px;font-size:33px;font-weight:900;color:var(--white);letter-spacing:.5px;line-height:38px;white-space:nowrap}
.hero-copy{left:549px;top:223px;width:240px;font-size:11.2px;line-height:18px;color:#f1f1f1;font-weight:300}
.hero-btn{left:550px;top:296px;width:95px;height:26px;border:1px solid var(--white);color:var(--white);font-size:8.5px;display:flex;align-items:center;justify-content:center}
.hero-arrow{top:139px;width:38px;height:38px;background:rgba(0,0,0,.25);display:flex;align-items:center;justify-content:center}

.section-title{font-size:20px;font-weight:300;color:#444}
.service{top:468px;width:170px;text-align:center}
.service svg{display:block;margin:0 auto}
.service h3{font-size:10px;font-weight:700;margin-top:16px;color:#2b2b2b}
.service p{font-size:8px;line-height:12.7px;color:var(--muted);margin-top:8px}
.service .more{font-size:7px;color:#555;margin-top:8px;display:block}

.mist{left:0;top:682px;width:1012px;height:334px;background:var(--mist);border-top:1px solid #e2e8eb}
.block-title{font-size:19px;font-weight:300;color:#444;white-space:nowrap}
.city{left:197px;top:761px;width:300px;height:107px;background:linear-gradient(180deg,#4a6fa6 0%,#2e4a7c 45%,#3a3450 75%,#b98a5a 100%)}
.about-copy{left:197px;top:891px;width:300px;font-size:7.8px;line-height:12.8px;color:var(--muted)}
.about-copy p+p{margin-top:12px}
.news{left:516px;width:300px;height:90px}
.news .thumb{position:absolute;left:0;top:0;width:88px;height:90px}
.news .date{position:absolute;left:8px;top:0;width:31px;height:32px;background:#333b40;color:var(--white);text-align:center}
.news .date small{display:block;font-size:6.5px;padding-top:4px}
.news .date b{display:block;font-size:17px;font-weight:300;line-height:16px}
.news h4{position:absolute;left:106px;top:2px;width:195px;font-size:11.5px;font-weight:400;line-height:16.5px;color:#333;white-space:nowrap}
.news p{position:absolute;left:106px;top:45px;width:190px;font-size:7.6px;line-height:12.6px;color:var(--muted)}

.footer{left:0;top:1016px;width:1012px;height:146px;background:var(--footer)}
.footer-brand{left:218px;top:1074px;color:var(--white);font-size:17px;font-weight:700;letter-spacing:4px;display:flex;align-items:center;gap:8px}
.footer-brand .mark{width:12px;height:12px;background:var(--white)}
.f-head{font-size:10px;font-weight:700;color:var(--white)}
.f-list{font-size:8px;color:var(--footer-text);line-height:19px;list-style:none}
.f-list li::before{content:"›";margin-right:6px}
.f-text{font-size:8px;color:#c3c8cb;line-height:14px}
.email-field{left:497px;top:1110px;width:103px;height:23px;background:#1f2327;color:#d0d4d6;font-size:8px;padding:7px 7px}
.subscribe{left:599px;top:1110px;width:56px;height:23px;background:var(--red);color:var(--white);font-size:8.5px;display:flex;align-items:center;justify-content:center}
.contact-row{position:absolute;left:688px;display:flex;gap:10px;font-size:8px;color:var(--footer-text);line-height:12.6px}
.contact-row svg{flex:none;margin-top:1px}
.bottombar{left:0;top:1162px;width:1012px;height:38px;background:var(--footer-deep);font-size:7px;color:var(--footer-text)}
</style>
</head>
<body>

<div class="abs topbar">
  <div class="item" style="left:614px">
    <svg width="12" height="9" viewBox="0 0 12 9"><rect x=".5" y=".5" width="11" height="8" fill="none" stroke="#fff"/><path d="M.5 .5 6 5 11.5 .5" fill="none" stroke="#fff"/></svg>
    hello@plenvaro-mail.com
  </div>
  <div class="item" style="left:741px">
    <svg width="10" height="10" viewBox="0 0 10 10"><path d="M2 1 4 3 3 4.2C3.7 5.6 4.4 6.3 5.8 7L7 6 9 8 7.8 9.3C4.5 8.8 1.2 5.5.7 2.2Z" fill="none" stroke="#fff" stroke-width=".9"/></svg>
    +88 900 246 135
  </div>
</div>

<header class="abs header">
  <div class="abs brand"><span class="mark"></span>PLENVARO</div>
  <nav class="nav">
    <a style="left:441px">Home</a>
    <a style="left:493px">Business Units</a>
    <a style="left:579px">Services</a>
    <a style="left:640px">About Us</a>
    <a style="left:705px">Locations</a>
    <a style="left:771px">Contact Us</a>
  </nav>
</header>

<section class="abs hero">
  <div class="hero-photo" role="img" aria-label="Photo of two engineers in hard hats reviewing site plans in front of a building under construction"></div>
  <div class="hero-panel"></div>
  <div class="abs hero-arrow" style="left:0">
    <svg width="8" height="12" viewBox="0 0 8 12"><path d="M6 1 1.5 6 6 11" fill="none" stroke="#fff" stroke-width="1.5"/></svg>
  </div>
  <div class="abs hero-arrow" style="left:974px">
    <svg width="8" height="12" viewBox="0 0 8 12"><path d="M2 1 6.5 6 2 11" fill="none" stroke="#fff" stroke-width="1.5"/></svg>
  </div>
</section>
<div class="abs hero-kicker">SYSTEM KNOWLEDGE</div>
<div class="abs hero-title">DELIVERED</div>
<div class="abs hero-copy">Plenvaro specializes in delivering quality pro-fessional services and technical projects that support larger business goals.</div>
<div class="abs hero-btn">LEARN MORE</div>

<h2 class="abs section-title" style="left:0;width:1012px;text-align:center;top:421px">Our Services</h2>

<div class="abs service" style="left:235px">
  <svg width="72" height="72" viewBox="0 0 72 72">
    <circle cx="36" cy="36" r="30" fill="none" stroke="var(--red)" stroke-width="5"/>
    <rect x="25" y="32" width="14" height="7" rx="2" fill="var(--red)"/>
    <rect x="33" y="29" width="14" height="7" rx="2" fill="var(--red)" stroke="#fff" stroke-width="1"/>
    <circle cx="28" cy="40" r="1.8" fill="var(--red)"/><circle cx="36" cy="40" r="1.8" fill="var(--red)"/>
    <circle cx="44" cy="37" r="1.8" fill="var(--red)"/>
  </svg>
  <h3>Transportation</h3>
  <p>Fusce gravida tortor felis<br>Ac dictum risus sagittis id morbi posu<br>justo eleifend libero ultricies</p>
  <span class="more">LEAR MORE</span>
</div>
<div class="abs service" style="left:422px">
  <svg width="72" height="72" viewBox="0 0 72 72">
    <circle cx="36" cy="36" r="30" fill="none" stroke="var(--red)" stroke-width="5"/>
    <path d="M27 32 36 27 45 32Z" fill="var(--red)"/>
    <rect x="29" y="33" width="2" height="8" fill="var(--red)"/><rect x="33" y="33" width="2" height="8" fill="var(--red)"/>
    <rect x="37" y="33" width="2" height="8" fill="var(--red)"/><rect x="41" y="33" width="2" height="8" fill="var(--red)"/>
    <rect x="27" y="42" width="18" height="2" fill="var(--red)"/>
  </svg>
  <h3>Government</h3>
  <p>Fusce gravida tortor felis<br>Ac dictum risus sagittis id morbi posu<br>justo eleifend libero ultricies</p>
  <span class="more">LEAR MORE</span>
</div>
<div class="abs service" style="left:607px">
  <svg width="72" height="72" viewBox="0 0 72 72">
    <circle cx="36" cy="36" r="30" fill="none" stroke="var(--red)" stroke-width="5"/>
    <rect x="30" y="27" width="12" height="17" fill="var(--red)"/>
    <g fill="#fff"><rect x="32" y="29" width="2" height="2"/><rect x="38" y="29" width="2" height="2"/><rect x="32" y="33" width="2" height="2"/><rect x="38" y="33" width="2" height="2"/><rect x="32" y="37" width="2" height="2"/><rect x="38" y="37" width="2" height="2"/><rect x="35" y="40" width="2" height="4"/></g>
  </svg>
  <h3>Commercial Sectors</h3>
  <p>Fusce gravida tortor felis<br>Ac dictum risus sagittis id morbi posu<br>justo eleifend libero ultricies</p>
  <span class="more">LEAR MORE</span>
</div>

<section class="abs mist"></section>
<h2 class="abs block-title" style="left:197px;top:724px">Welcome to Plenvaro International</h2>
<div class="abs city" role="img" aria-label="Photo of a city skyline with lit towers at dusk"></div>
<div class="abs about-copy">
  <p>Maecenas bibendum lacus gravida placerat consequat. Vivamus quis hendrerit mauris. Vestibulum laoreet felis sed consectetur sollicitudin. Sed a mauris massa.</p>
  <p>Nullam interdum, elit nec facilisis iaculis, arcu enim condimentum tellus, ut convallis elit purus eu est. Interdum et malesuada fames ac ante ipsum primis in faucibus. Nullam odio nulla, commodo a dui at, pretium iaculis quam.</p>
</div>

<h2 class="abs block-title" style="left:516px;top:724px">Latest News</h2>
<article class="abs news" style="top:761px">
  <div class="thumb" role="img" aria-label="Photo of hands reviewing printed documents at a desk" style="background:linear-gradient(135deg,#e9ecef,#c9ced3 60%,#f4f5f6)"></div>
  <div class="date"><small>oct</small><b>18</b></div>
  <h4>Lorem ipsum dolor sit amet, consecte-<br>tur adipiscing</h4>
  <p>Maecenas bibendum lacus gravida placerat conse-quat. Vivamus quis hendrerit mauris. Vestibulum laoreet felis sed consectetur sollicitudin.</p>
</article>
<article class="abs news" style="top:868px">
  <div class="thumb" role="img" aria-label="Photo of two colleagues in a business meeting" style="background:linear-gradient(135deg,#f0f1f2,#b9c3cc 55%,#c9d36a 100%)"></div>
  <div class="date"><small>oct</small><b>18</b></div>
  <h4>Lorem ipsum dolor sit amet, consecte-<br>tur adipiscing</h4>
  <p>Maecenas bibendum lacus gravida placerat conse-quat. Vivamus quis hendrerit mauris. Vestibulum laoreet felis sed consectetur sollicitudin.</p>
</article>

<footer class="abs footer"></footer>
<div class="abs footer-brand"><span class="mark"></span>PLENVARO</div>

<div class="abs f-head" style="left:390px;top:1046px">Navigation</div>
<ul class="abs f-list" style="left:390px;top:1066px">
  <li>Home</li><li>Services</li><li>About</li><li>Blog</li>
</ul>

<div class="abs f-head" style="left:497px;top:1046px">Newsletter</div>
<div class="abs f-text" style="left:497px;top:1069px;width:150px">Ipsum dolor sit amet, teft consecte tur adipiscing elit ut eunt.</div>
<div class="abs email-field">Email Address</div>
<div class="abs subscribe">Subscribe</div>

<div class="abs f-head" style="left:688px;top:1046px">Contact Details</div>
<div class="contact-row" style="top:1070px">
  <svg width="10" height="10" viewBox="0 0 10 10"><path d="M2 1 4 3 3 4.2C3.7 5.6 4.4 6.3 5.8 7L7 6 9 8 7.8 9.3C4.5 8.8 1.2 5.5.7 2.2Z" fill="var(--footer-text)"/></svg>
  +1800-123-4567
</div>
<div class="contact-row" style="top:1089px">
  <svg width="10" height="9" viewBox="0 0 10 9"><rect x=".5" y=".5" width="9" height="8" fill="none" stroke="var(--footer-text)"/><path d="M.5 .5 5 4.5 9.5 .5" fill="none" stroke="var(--footer-text)"/></svg>
  info@yourwebsite.com
</div>
<div class="contact-row" style="top:1108px">
  <svg width="10" height="12" viewBox="0 0 10 12"><path d="M5 11.5C2 7.5 1 6 1 4.2A4 4 0 0 1 9 4.2C9 6 8 7.5 5 11.5Z" fill="var(--footer-text)"/><circle cx="5" cy="4.2" r="1.5" fill="var(--footer)"/></svg>
  <span>Your Address, Your Country<br>Your Zip Code</span>
</div>

<div class="abs bottombar">
  <span class="abs" style="left:197px;top:14px">Copyright © 2014 - Plenvaro International. All Rights reserved</span>
  <span class="abs" style="left:691px;top:14px">Privacy Policy &nbsp;|&nbsp; Sitemap</span>
</div>

</body>
</html>
```